Property Management Company Business Cards

Need business cards for a property management company located in Michigan. We manage houses for clients all over the world. Young and modern company, looking for eye catching design. Please work with the attached logo.

Industry/Entity Type

Property Management

Requirements
Must have
• Need lines for address, telephone number, fax number, web site.

Also lines for name, and job title

```html
<!DOCTYPE html>
<html lang="en">
<head>
<meta charset="utf-8">
<title>Lakeshore Harbor Management – Business Cards</title>
<link rel="stylesheet" href="https://fonts.googleapis.com/css2?family=Source+Sans+3:wght@400;600;700&display=swap">
<style>
  :root {
    --page-bg: #ffffff;
    --card-white: #ffffff;
    --brand-blue: #0aa1dd;
    --ink-dark: #222222;
    --text-light: #ffffff;
    --card-shadow: 0 2px 8px rgba(0, 0, 0, 0.28);
  }
  * { margin: 0; padding: 0; box-sizing: border-box; }
  html, body {
    width: 1200px;
    height: 1000px;
    overflow: hidden;
    background: var(--page-bg);
    font-family: "Source Sans 3", "Myriad Pro", Arial, sans-serif;
  }
  .canvas { position: relative; width: 1200px; height: 1000px; }

  .card {
    position: absolute;
    left: 273px;
    width: 653px;
    height: 363px;
    box-shadow: var(--card-shadow);
  }
  .card--front { top: 130px; background: var(--card-white); }
  .card--back  { top: 507px; background: var(--brand-blue); color: var(--text-light); }

  /* Front: wordmark */
  .wordmark {
    position: absolute;
    left: 95px;
    top: 142px;
    display: flex;
    align-items: center;
    gap: 18px;
  }
  .wordmark__dot {
    width: 74px;
    height: 74px;
    border-radius: 50%;
    background: var(--ink-dark);
    flex-shrink: 0;
  }
  .wordmark__name {
    color: var(--ink-dark);
    font-weight: 700;
    font-size: 34px;
    line-height: 1;
    letter-spacing: -0.5px;
    text-transform: uppercase;
  }
  .wordmark__name span { display: block; }
  .wordmark__name span + span { font-size: 20px; letter-spacing: 15.5px; margin-top: 4px; }

  /* Back: identity */
  .identity {
    position: absolute;
    left: 237px;
    top: 61px;
    display: flex;
    align-items: center;
    gap: 21px;
  }
  .identity__dot {
    width: 68px;
    height: 68px;
    border-radius: 50%;
    background: var(--text-light);
  }
  .identity__name { font-weight: 700; font-size: 21px; line-height: 1.1; }
  .identity__role { color: var(--ink-dark); font-size: 16px; line-height: 1.2; }

  .contact {
    position: absolute;
    left: 0;
    right: 0;
    top: 234px;
    text-align: center;
    font-size: 17px;
    line-height: 24px;
    letter-spacing: 0.4px;
  }
  .contact__row { display: flex; justify-content: center; gap: 30px; }
  .contact__label { color: var(--ink-dark); font-weight: 700; margin-right: 7px; }

  .address {
    position: absolute;
    left: 0;
    right: 0;
    top: 329px;
    text-align: center;
    font-size: 17px;
    letter-spacing: 0.4px;
  }
</style>
</head>
<body>
<main class="canvas">
  <section class="card card--front" aria-label="Card front">
    <div class="wordmark">
      <div class="wordmark__dot"></div>
      <p class="wordmark__name"><span>Lakeshore Harbor</span><span>Management</span></p>
    </div>
  </section>

  <section class="card card--back" aria-label="Card back">
    <div class="identity">
      <div class="identity__dot"></div>
      <div>
        <p class="identity__name">NAME</p>
        <p class="identity__role">Job Position</p>
      </div>
    </div>

    <div class="contact">
      <p class="contact__row">
        <span><span class="contact__label">T</span>555-210-3381</span>
        <span><span class="contact__label">F</span>555-210-3389</span>
      </p>
      <p><span class="contact__label">W</span>www.lakeshoreharbor.com</p>
    </div>

    <p class="address">18420 Maple Lane, Novi, Michigan, 48375</p>
  </section>
</main>
</body>
</html>
```